Elegant eBook Word Template Design Required

I need an ebook template designed to match my website branding. It needs to include index, intro, chapters and about me. Word format required.

I will be using this template to create downloadable pdfs on my website.

For branding visit my website http://ravelkostin.com.au

Facebook: @RavelKostinOnline

Target Market(s)

Business owners, Entrepreneurs

Industry/Entity Type

Business Consultant

Font styles to use
Other font styles liked:
• check website

Colors

Designer to choose colors to be used in the design.

Requirements
Must have
• - Font and colour scheme must match my website branding

```html
<!DOCTYPE html>
<html lang="en">
<head>
<meta charset="utf-8">
<title>Ravel Kostin eBook Template</title>
<link rel="stylesheet" href="https://fonts.googleapis.com/css2?family=Montserrat:wght@400;600;700&family=Oswald:wght@500&display=swap">
<style>
:root{
  --stage:#e4e5e7;
  --paper:#ffffff;
  --brand:#4a9cc4;
  --brand-light:#5cc2e6;
  --ink:#3a3a3c;
  --ink-soft:#7b7d80;
  --rule:#9a9ca0;
}
*{margin:0;padding:0;box-sizing:border-box}
html,body{width:1200px;height:360px;overflow:hidden;background:var(--stage)}
body{position:relative;font-family:"Montserrat",sans-serif;color:var(--ink);font-size:4px;line-height:1.4}
.page{position:absolute;top:24px;width:231px;height:314px;background:var(--paper);box-shadow:2px 3px 6px rgba(0,0,0,.28);overflow:hidden}
.page--cover{left:6px}
.page--about{left:250px}
.page--contents{left:488px}
.page--chapter{left:725px}
.page--back{left:964px;width:230px;background:var(--brand);color:#fff}

.brand{position:absolute;left:0;right:0;top:12px;text-align:center;z-index:2}
.brand-mark{display:block;width:20px;height:20px;margin:0 auto 7px;background:var(--brand)}
.brand-name{display:block;font-weight:700;font-size:9.5px;line-height:1.1;letter-spacing:.3px;color:var(--ink)}

.page-bar{position:absolute;left:0;bottom:6px;width:48px;height:3px;background:var(--brand)}
.page--back .page-bar{background:#fff}

/* cover */
.cover-art{position:absolute;left:0;top:52px;width:231px;height:218px;z-index:1}
.cover-title{position:absolute;left:118px;top:178px;z-index:2;font-family:"Oswald",sans-serif;font-weight:500;color:#fff;line-height:1.05}
.cover-title .line1{display:block;font-size:15.5px}
.cover-title .line2{display:block;font-size:20px;letter-spacing:.3px}
.cover-blurb{position:absolute;left:11px;top:273px;width:100px;font-size:3.6px;line-height:1.45;color:var(--ink)}
.cover-address{position:absolute;left:118px;top:274px;font-size:3.4px;line-height:1.5;color:var(--ink);border-left:.5px solid var(--rule);padding-left:4px}
.cover-services{position:absolute;left:11px;top:302px;font-size:4.6px;line-height:1;font-weight:700;letter-spacing:.9px;color:var(--ink)}
.cover-services .dot{color:var(--brand-light)}

/* about */
.about-photo{position:absolute;left:28px;top:64px;width:72px;height:66px}
.about-quote{position:absolute;left:104px;top:64px;width:100px;height:66px;background:var(--brand);color:#fff;padding:6px 6px 0 7px;font-size:4.4px;line-height:1.4}
.about-quote p{margin-bottom:4px}
.about-quote cite{font-style:normal;font-size:3.2px}
.about-body{position:absolute;left:28px;top:136px;width:180px;font-size:3.7px;line-height:1.42}
.about-body p{margin-bottom:3.3px}
.about-body strong{font-weight:700}
.section-title{position:absolute;left:28px;font-weight:600;line-height:1;color:var(--ink)}
.section-title--about{top:286px;font-size:15px;letter-spacing:.4px}

/* contents */
.contents-title{position:absolute;left:0;right:0;top:70px;text-align:center;font-weight:600;font-size:12.5px;line-height:1;letter-spacing:.8px;color:var(--brand-light)}
.contents-intro{position:absolute;left:24px;width:184px;top:93px;font-size:3.5px;line-height:1.45;text-align:center;color:var(--ink-soft)}
.toc{position:absolute;left:24px;top:123px;width:184px;list-style:none;font-size:3.6px;color:var(--ink-soft)}
.toc-group{margin-bottom:7px}
.toc-chapter{font-size:4.4px;line-height:1.3;font-weight:600;color:var(--brand-light);margin-bottom:1.5px;letter-spacing:.3px}
.toc-item{display:flex;line-height:1.5}
.toc-item .leader{flex:1;border-bottom:.5px dashed var(--rule);margin:0 1px 1.6px}

/* chapter */
.chapter-body{position:absolute;left:24px;top:54px;width:184px;height:222px;overflow:hidden;font-size:3.5px;line-height:1.45;color:var(--ink-soft)}
.chapter-body p{margin-bottom:4px}
.section-title--chapter{left:24px;top:294px;font-size:10.5px;color:var(--brand-light);letter-spacing:.5px}

/* back */
.back-brand{position:absolute;left:0;right:0;top:204px;text-align:center}
.back-brand .brand-mark{width:34px;height:34px;background:#fff;margin-bottom:5px}
.back-brand .brand-name{color:#fff;font-size:5.5px;line-height:1}
.back-contact{position:absolute;left:0;right:0;top:258px;text-align:center;font-size:4.3px;font-weight:600;line-height:1.75}
.social{display:flex;justify-content:center;gap:3px;margin-top:2px}
.social span{width:7px;height:7px;border-radius:50%;border:.6px solid #fff}
</style>
</head>
<body>

<section class="page page--cover">
  <div class="brand"><span class="brand-mark"></span><span class="brand-name">RAVEL KOSTIN</span></div>
  <svg class="cover-art" viewBox="0 0 231 218" role="img" aria-label="Geometric blue faceted illustration with city towers">
    <defs>
      <linearGradient id="coverGrad" x1="0" y1="0" x2="1" y2="1">
        <stop offset="0" stop-color="#7fdcf2"/>
        <stop offset=".5" stop-color="#4aa8e4"/>
        <stop offset="1" stop-color="#5a6fd8"/>
      </linearGradient>
    </defs>
    <polygon points="0,8 115,0 231,18 231,190 150,218 0,202" fill="url(#coverGrad)"/>
  </svg>
  <h1 class="cover-title"><span class="line1">THE POWER OF</span><span class="line2">GRATITUDE</span></h1>
  <p class="cover-blurb">Maecenas eget molestie nunc. Aliquam elementum lectus et tristique scelerisque, odio augue tempor lectus, sit amet eleifend elit massa et metus. Sed ac ultrices diam.</p>
  <p class="cover-address">27 Linden Way<br>NA 40417<br>Harlow Bay<br><br>+1 1234 5678<br>www.yourwebsite.com</p>
  <p class="cover-services">COACHING <span class="dot">•</span> CONSULTING <span class="dot">•</span> TRAININGS</p>
</section>

<section class="page page--about">
  <div class="about-photo" role="img" aria-label="Portrait video still of the author" style="background:linear-gradient(135deg,#8a8f96,#3b4150)"></div>
  <blockquote class="about-quote">
    <p>“There is a beautiful part of us, a deeper part of us, that when we get in tune with, we can grow beyond tough circumstances.</p>
    <p>It’s like a lotus that glows beautifully and floats in a dirty pond”</p>
    <cite>– Ravel Kostin</cite>
  </blockquote>
  <div class="about-body">
    <p>I grew up in a challenged, poor neighbourhood in Mumbai. There, myself and 13 others all lived in a single bedroom on the fifth floor of an old dingy apartment. It was a bedroom that wouldn’t be any larger than a western kitchen.</p>
    <p>So I’m humbled to have experienced limitations of life. I know what it’s like. And more importantly, I know it is not the be all and end all.</p>
    <p>In fact, it was far from it. You see, no matter how tough it seemed, each day from the fifth storey of our apartment, I saw below us, the real slums of Mumbai. There, people were living with no shelter, no food, no water...and certainly no toilets.</p>
    <p>If you think you are on the ground floor, look around you and you’ll see that there are basements about.</p>
    <p>So I realized I actually had it pretty good.</p>
    <p>When I decided to be grateful for what I had, things just fell in place. I took opportunities as they came, studied hard, got scholarships, and before I knew it...I was being sent off to America to get a degree in engineering!</p>
    <p>Things just fell in place.</p>
    <p>I graduated from university, got myself a Master’s degree, published many papers and patents in the space of engineering and IT technology, and ended up with a high paying job during an economic downturn!</p>
    <p><strong>Being Grateful for What I Had, Gave Me Access to More Opportunities!</strong></p>
    <p>So what are you thankful for today?</p>
  </div>
  <h2 class="section-title section-title--about">ABOUT ME</h2>
  <span class="page-bar"></span>
</section>

<section class="page page--contents">
  <div class="brand"><span class="brand-mark"></span><span class="brand-name">RAVEL KOSTIN</span></div>
  <h2 class="contents-title">CONTENTS</h2>
  <p class="contents-intro">Lorem ipsum dolor sit amet, consectetur adipiscing elit. Quisque ultricies, ante vel euismod mattis, felis sem. Lorem ipsum dolor sit amet, consectetur adipiscing elit. Quisque ultricies, ante vel euismod mattis, felis sem lorem ipsum dolor sit amet.</p>
  <ul class="toc">
    <li class="toc-group">
      <div class="toc-item"><span>Lorem ipsum dolor sit a adipiscing elit, Quisque</span><span class="leader"></span><span>1</span></div>
      <div class="toc-item"><span>Lorem ipsum dolor sit amet, e</span><span class="leader"></span><span>4</span></div>
    </li>
    <li class="toc-group">
      <div class="toc-chapter">LOREL IMPSUM CHAPTER 1</div>
      <div class="toc-item"><span>Lorem ipsum dolorg slit. Quisque</span><span class="leader"></span><span>11</span></div>
      <div class="toc-item"><span>Lorem ipsum dolor sit amet, e</span><span class="leader"></span><span>14</span></div>
      <div class="toc-item"><span>Lorem ipsum dolorg slit. Quisque</span><span class="leader"></span><span>11</span></div>
      <div class="toc-item"><span>Lorem ipsum dolor sit amet, e</span><span class="leader"></span><span>14</span></div>
    </li>
    <li class="toc-group">
      <div class="toc-chapter">LOREL IMPSUM CHAPTER 2</div>
      <div class="toc-item"><span>Lorem ipsum dolorg slit. Quisque</span><span class="leader"></span><span>11</span></div>
      <div class="toc-item"><span>Lorem ipsum dolor sit amet, e</span><span class="leader"></span><span>14</span></div>
      <div class="toc-item"><span>Lorem ipsum dolorg slit. Quisque</span><span class="leader"></span><span>11</span></div>
      <div class="toc-item"><span>Lorem ipsum dolor sit amet, e</span><span class="leader"></span><span>14</span></div>
    </li>
    <li class="toc-group">
      <div class="toc-chapter">LOREL IMPSUM CHAPTER 3</div>
      <div class="toc-item"><span>Lorem ipsum dolorg slit. Quisque</span><span class="leader"></span><span>11</span></div>
      <div class="toc-item"><span>Lorem ipsum dolor sit amet, e</span><span class="leader"></span><span>14</span></div>
    </li>
    <li class="toc-group">
      <div class="toc-chapter">LOREL IMPSUM CHAPTER 4</div>
      <div class="toc-item"><span>Lorem ipsum dolorg slit. Quisque</span><span class="leader"></span><span>11</span></div>
      <div class="toc-item"><span>Lorem ipsum dolor sit amet, e</span><span class="leader"></span><span>14</span></div>
      <div class="toc-item"><span>Lorem ipsum dolorg slit. Quisque</span><span class="leader"></span><span>11</span></div>
      <div class="toc-item"><span>Lorem ipsum dolor sit amet, e</span><span class="leader"></span><span>14</span></div>
    </li>
  </ul>
  <span class="page-bar"></span>
</section>

<section class="page page--chapter">
  <div class="brand"><span class="brand-mark"></span><span class="brand-name">RAVEL KOSTIN</span></div>
  <div class="chapter-body">
    <p>Lorem ipsum dolor sit amet, consectetur adipiscing elit. Quisque ultricies, ante vel euismod mattis, felis sem.Lorem ipsum dolor sit amet, consectetur adipiscing elit. Quisque ultricies, ante vel euismod mattis, felis sem lorem ipsum dolor sit amet.</p>
    <p>Lorem ipsum dolor sit amet, consectetur adipiscing elit. Quisque ultricies, ante vel euismod mattis, felis sem.Lorem ipsum dolor sit amet, consectetur adipiscing elit. Quisque ultricies, ante vel euismod mattis, felis sem lorem ipsum dolor sit amet, consectetur adipiscing elit. Quisque ultricies, ante vel euismod mattis, felis sem lorem ipsum dolor sit amet, consectetur adipiscing elit.</p>
    <p>Lorem ipsum dolor sit amet, consectetur adipiscing elit. Quisque ultricies, ante vel euismod mattis, felis sem.Lorem ipsum dolor sit amet, consectetur adipiscing elit. Quisque ultricies, ante vel euismod mattis, felis sem lorem ipsum dolor sit amet, consectetur adipiscing elit. Quisque ultricies, ante vel euismod mattis, felis sem lorem ipsum dolor sit amet, consectetur adipiscing elit. Quisque ultricies, ante vel euismod mattis, felis sem lorem ipsum dolor sit amet, consectetur adipiscing elit. Quisque ultricies, ante vel euismod mattis, felis sem lorem ipsum dolor sit amet, consectetur adipiscing elit. Quisque ultricies, ante vel euismod mattis, felis sem lorem ipsum dolor sit amet, consectetur adipiscing elit. Quisque ultricies, ante vel euismod mattis, felis sem lorem ipsum dolor sit amet.</p>
    <p>Lorem ipsum dolor sit amet, consectetur adipiscing elit. Quisque ultricies, ante vel euismod mattis, felis sem.Lorem ipsum dolor sit amet, consectetur adipiscing elit. Quisque ultricies, ante vel euismod mattis, felis sem lorem ipsum dolor sit amet, consectetur adipiscing elit. Quisque ultricies, ante vel euismod mattis, felis sem lorem ipsum dolor sit amet, consectetur adipiscing elit. Quisque ultricies, ante vel euismod mattis, felis sem lorem ipsum dolor sit amet, consectetur adipiscing elit. Quisque ultricies, ante vel euismod mattis, felis sem lorem ipsum dolor sit amet.</p>
    <p>Lorem ipsum dolor sit amet, consectetur adipiscing elit. Quisque ultricies, ante vel euismod mattis, felis sem.Lorem ipsum dolor sit amet, consectetur adipiscing elit. Quisque ultricies.</p>
    <p>Lorem ipsum dolor sit amet, consectetur adipiscing elit. Quisque ultricies, ante vel euismod mattis, felis sem lorem ipsum dolor sit amet, consectetur adipiscing elit.</p>
    <p>vel euismod mattis, felis sem lorem ipsum dolor sit amet.</p>
  </div>
  <h2 class="section-title section-title--chapter">CHAPTER 1</h2>
  <span class="page-bar"></span>
</section>

<section class="page page--back">
  <div class="back-brand"><span class="brand-mark"></span><span class="brand-name">RAVEL KOSTIN</span></div>
  <div class="back-contact">
    <p>48 Harbour Lane, Port Melville, VIC 3299</p>
    <p>+61 3 9000 4127</p>
    <p>ravel@ravelkostin.com.au</p>
    <div class="social"><span></span><span></span><span></span><span></span><span></span></div>
  </div>
  <span class="page-bar"></span>
</section>

</body>
</html>
```